Personal Training

Personal Fitness Trainer
Sports Nutritionist
Individual and Group rates available
Certifications
Global Wellness Coaching Federation
Continental Athletic Studies Council

Industry/Entity Type

Fitness

Contact Information for Business Card

Dorinda Pellham
555-284-7163
vetrubel4@quintmail.example

```html
<!DOCTYPE html>
<html lang="en">
<head>
<meta charset="utf-8">
<title>Dorinda Pellham – Personal Training Business Card</title>
<link rel="stylesheet" href="https://fonts.googleapis.com/css2?family=Audiowide&family=Varela+Round&display=swap">
<style>
  :root {
    --page: #ebebeb;
    --card-white: #ffffff;
    --pink: #d9466c;
    --charcoal: #4b4b4d;
    --stripe: #3f3f41;
    --photo-light: #d8d8d8;
    --photo-dark: #6e6e6e;
    --text-light: #ffffff;
  }
  * { margin: 0; padding: 0; box-sizing: border-box; }
  html, body { width: 1200px; height: 849px; overflow: hidden; background: var(--page); }
  .canvas {
    position: relative; width: 1200px; height: 849px;
    display: flex; align-items: center; justify-content: center; gap: 40px;
  }
  .card {
    position: relative; width: 540px; height: 309px; overflow: hidden;
    box-shadow: 0 6px 18px rgba(0,0,0,0.18);
  }
  .card svg.card-art { position: absolute; inset: 0; width: 100%; height: 100%; }
  .name {
    position: absolute; right: 28px; text-align: right;
    font-family: "Audiowide", sans-serif; line-height: 1; letter-spacing: 1px;
  }
  .name .first { display: block; color: var(--pink); font-size: 24px; }
  .name .last { display: block; font-size: 30px; margin-top: 2px; }
  .card-front .name { top: 20px; }
  .card-front .name .last { color: var(--stripe); }
  .services {
    position: absolute; left: 34px; top: 152px;
    font-family: "Varela Round", sans-serif; font-size: 16px; line-height: 1.32;
    color: var(--text-light); list-style: none;
  }
  .card-back { background: var(--charcoal); }
  .card-back .name { top: 92px; right: 36px; }
  .card-back .name .last { color: var(--text-light); }
  .contact {
    position: absolute; right: 36px; top: 200px; text-align: right;
    font-family: "Varela Round", sans-serif; font-size: 17px; color: var(--text-light);
    list-style: none;
  }
  .contact li { display: flex; align-items: center; justify-content: flex-end; gap: 8px; margin-bottom: 14px; }
  .contact svg { width: 16px; height: 16px; flex: none; }
</style>
</head>
<body>
<main class="canvas">

  <section class="card card-front" aria-label="Business card front">
    <svg class="card-art" viewBox="0 0 540 309" aria-hidden="true">
      <rect width="540" height="309" fill="var(--card-white)"/>
      <path d="M0,118 C140,92 320,150 540,88 L540,100 C320,162 140,104 0,132 Z" fill="var(--stripe)"/>
      <path d="M0,140 C150,114 320,172 540,112 L540,309 L0,309 Z" fill="var(--pink)"/>
    </svg>
    <h1 class="name"><span class="first">DORINDA</span><span class="last">PELLHAM</span></h1>
    <ul class="services">
      <li>Personal Fitness Trainer</li>
      <li>Sports Nutritionist</li>
      <li>Individual and Group rates available</li>
      <li>Certifications</li>
      <li>Global Wellness Coaching Federation</li>
      <li>Continental Athletic Studies Council</li>
    </ul>
  </section>

  <section class="card card-back" aria-label="Business card back">
    <svg class="card-art" viewBox="0 0 540 309">
      <defs>
        <linearGradient id="photoTone" x1="0" y1="0" x2="0" y2="1">
          <stop offset="0" stop-color="var(--photo-light)"/>
          <stop offset="1" stop-color="var(--photo-dark)"/>
        </linearGradient>
      </defs>
      <path d="M0,309 L0,0 L225,0 C160,60 170,130 200,190 C230,250 250,280 238,309 Z" fill="var(--card-white)"/>
      <path d="M236,0 C172,60 182,130 212,190 C242,250 262,280 250,309" fill="none" stroke="var(--pink)" stroke-width="6"/>
      <path role="img" aria-label="Black and white photo of the trainer posing outdoors" d="M0,309 L0,0 L208,0 C146,60 156,130 186,190 C216,250 236,280 224,309 Z" fill="url(#photoTone)"/>
    </svg>
    <h2 class="name"><span class="first">DORINDA</span><span class="last">PELLHAM</span></h2>
    <ul class="contact">
      <li>
        <svg viewBox="0 0 16 16" aria-hidden="true"><circle cx="8" cy="8" r="8" fill="var(--pink)"/><path d="M5,4 L7,4 L7.5,6 L6.5,7 C7,8.3 7.7,9 9,9.5 L10,8.5 L12,9 L12,11 C8,11.5 4.5,8 5,4 Z" fill="var(--text-light)"/></svg>
        <span>555-284-7163</span>
      </li>
      <li>
        <svg viewBox="0 0 16 16" aria-hidden="true"><circle cx="8" cy="8" r="8" fill="var(--pink)"/><rect x="4" y="5" width="8" height="6" fill="none" stroke="var(--text-light)" stroke-width="1.2"/><path d="M4,5 L8,8.5 L12,5" fill="none" stroke="var(--text-light)" stroke-width="1.2"/></svg>
        <span>vetrubel4@quintmail.example</span>
      </li>
    </ul>
  </section>

</main>
</body>
</html>
```